New (old) Business Card Design Project

I would like to purchase a customized version of a design you have previously submitted - https://www.artmarketly.example/design/7305126

I like the card above, and would like to use the same design, jus with my business name, HARLOWAY ASSET ADVISORS. I like the colors in the card above, as well as the font. The other side will have my name, company name, address, phone, email, website, plus disclosure text I will provide.

Target Market(s)

wealthy families

Industry/Entity Type

Financial Services

Contact Information for Business Card

logo on one side, on other my name, company, address, phone, email, website, disclosure language I will provide.

Colors

Designer to choose colors to be used in the design.

Requirements
Must have
• colors: Deep blue and white
Nice to have
• Please see the items I have uploaded, below.
Should not have
• Cheap, tacky look.

```html
<!DOCTYPE html>
<html lang="en">
<head>
<meta charset="utf-8">
<title>Harloway Asset Advisors – Business Card</title>
<link rel="stylesheet" href="https://fonts.googleapis.com/css2?family=Source+Sans+3:wght@400;600;700&display=swap">
<style>
  :root {
    --navy: #1b2b57;
    --navy-deep: #16244b;
    --paper: #ffffff;
    --ink: #1d1d1d;
    --stage: #2c2c2c;
  }
  * { box-sizing: border-box; margin: 0; padding: 0; }
  html, body {
    width: 1200px;
    height: 866px;
    overflow: hidden;
    background: var(--stage);
    font-family: "Source Sans 3", sans-serif;
  }
  .sheet {
    position: relative;
    width: 1200px;
    height: 866px;
  }
  .card {
    position: absolute;
    top: 284px;
    width: 520px;
    height: 298px;
    box-shadow: 0 10px 24px rgba(0,0,0,0.45);
  }
  .card--front {
    left: 50px;
    background: var(--navy);
    display: flex;
    align-items: center;
    justify-content: center;
  }
  .card__texture {
    position: absolute;
    inset: 0;
    background: linear-gradient(135deg, var(--navy) 0%, var(--navy-deep) 100%);
  }
  .brand-name {
    position: relative;
    color: var(--paper);
    font-weight: 400;
    font-size: 25px;
    letter-spacing: 0.14em;
    text-transform: uppercase;
    white-space: nowrap;
  }
  .card--back {
    left: 630px;
    background: var(--paper);
  }
  .person {
    position: absolute;
    left: 62px;
    top: 62px;
    text-transform: uppercase;
  }
  .person__name {
    color: var(--navy);
    font-weight: 700;
    font-size: 20px;
    letter-spacing: 0.02em;
  }
  .person__role {
    color: var(--ink);
    font-size: 13px;
    letter-spacing: 0.03em;
  }
  .divider {
    position: absolute;
    left: 238px;
    top: 118px;
    width: 1px;
    height: 130px;
    background: var(--navy);
  }
  .contact {
    position: absolute;
    left: 256px;
    top: 142px;
    list-style: none;
    color: var(--ink);
    font-size: 14px;
    line-height: 1.35;
  }
  .contact__label {
    color: var(--navy);
    font-weight: 700;
  }
  .contact__domain { color: var(--navy); }
</style>
</head>
<body>
<main class="sheet">
  <section class="card card--front" aria-label="Card front">
    <div class="card__texture" role="img" aria-label="Deep blue background with faint repeated name pattern"></div>
    <p class="brand-name">Harloway Asset Advisors</p>
  </section>

  <section class="card card--back" aria-label="Card back">
    <div class="person">
      <p class="person__name">Edmund Carrow</p>
      <p class="person__role">Managing Director</p>
    </div>
    <div class="divider"></div>
    <ul class="contact">
      <li><span class="contact__label">TEL:</span> 044-555 210 376</li>
      <li><span class="contact__label">EMAIL:</span> info@harloway.example</li>
      <li>www.<span class="contact__domain">harloway</span>.example</li>
      <li>18 Calder Row, Suite 4</li>
      <li>Eastmoor, 60218</li>
    </ul>
  </section>
</main>
</body>
</html>
```